NOT HAPPY FLYER

The brochure is for a Real Estate Agent, as a prospecting tool for upmarket, expensive homes.

BRIEF:
On the first side will be:
NOT HAPPY? (in a funky font)
(Have a picture of maybe an unhappy dog, or something that displays unhappiness on the front)

The second side:
-With your current service and advice?
Need a result NOW?
-Want a second opinion?

If you have been on the market for over 45 days with no results, it’s time to question why.

Tessa Brindley (photo of Tessa)
Your Modern, Local Real Estate Agent.

It is no secret that the greater the exposure a property has to the market, the greater the number of buyers who are aware of the listing. Every property is unique and Tessa ensures that each property has its own tailored marketing plan, so your property stands out from the crowd.

Whether you’re considering buying locally or internationally, Tessa will work with you to towards understanding those special qualities and those requirements you seek.
If you want to combine these components into an advantageous world class real estate transaction, call Tessa Brindley.

W: (WEBSITE HERE)
M: (MOBILE HERE)
E: (EMAIL HERE)

Target Market(s)

The target market are people who own upmarket, expensive properties.

Industry/Entity Type

Real Estate

Font styles to use
Decorative

Requirements
Must have
• Must be fun, yet professional. Needs to stand out. It will be printed in matt gloss laminate, so it will look very exclusive.

Second side with my photo and a small Hovex logo
Nice to have
• Have some funky fonts.

```html
<!DOCTYPE html>
<html lang="en">
<head>
<meta charset="utf-8">
<title>Not Happy Flyer – Tessa Brindley</title>
<link href="https://fonts.googleapis.com/css2?family=Chewy&family=Lato:wght@400;700;900&display=swap" rel="stylesheet">
<style>
  :root {
    --red: #d10a0f;
    --red-dark: #8e0206;
    --black: #0b0b0b;
    --charcoal: #2c2c2c;
    --grey-light: #9a9a9a;
    --white: #ffffff;
    --backdrop: #d7d7d7;
    --photo-warm: #b89a7c;
    --photo-cream: #e8ddd0;
  }
  * { box-sizing: border-box; margin: 0; padding: 0; }
  html, body { width: 1200px; height: 900px; overflow: hidden; }
  body { background: var(--backdrop); font-family: "Lato", sans-serif; position: relative; }

  .page { position: absolute; overflow: hidden; box-shadow: 0 6px 18px rgba(0,0,0,.35); }
  .page-bg { position: absolute; inset: 0; width: 100%; height: 100%; }

  /* Front */
  .front { left: 55px; top: 80px; width: 530px; height: 740px; }
  .headline {
    position: absolute; left: 24px; top: 548px;
    font-family: "Chewy", cursive; font-weight: 400; font-size: 64px; line-height: 1.02; letter-spacing: 5px;
  }
  .headline .not { color: var(--white); -webkit-text-stroke: 2px var(--black); display: block; }
  .headline .happy { color: var(--black); -webkit-text-stroke: 1.5px var(--white); display: block; }

  /* Back */
  .back { left: 628px; top: 78px; width: 532px; height: 744px; }
  .questions { position: absolute; left: 33px; top: 26px; width: 466px; }
  .question { color: var(--white); font-weight: 700; font-size: 13px; line-height: 16px; margin-bottom: 10px; }
  .answer-box { background: var(--white); height: 28px; margin-bottom: 10px; }
  .answer-box.tall { height: 87px; }

  .intro {
    position: absolute; left: 33px; top: 450px; width: 276px;
    color: var(--white); font-size: 11px; line-height: 13.5px; text-align: justify; hyphens: auto;
  }
  .intro p + p { margin-top: 13px; }
  .intro .agent-name { color: var(--red); font-weight: 700; }

  .agent-photo {
    position: absolute; left: 333px; top: 386px; width: 164px; height: 222px;
    border: 4px solid var(--white);
    background: linear-gradient(160deg, #5f7a4a 0%, #3b4a2e 45%, #6b4a38 70%, #1c1c1c 100%);
    box-shadow: 0 3px 8px rgba(0,0,0,.5);
  }
  .name-pill {
    position: absolute; left: 352px; top: 620px; width: 130px; height: 26px;
    background: linear-gradient(#ffffff, #d9d9d9); border-radius: 13px;
    color: var(--charcoal); font-weight: 900; font-size: 12.5px;
    display: flex; align-items: center; justify-content: center;
    box-shadow: 0 2px 5px rgba(0,0,0,.5);
  }
  .brand {
    position: absolute; left: 33px; top: 676px; width: 44px;
    display: flex; flex-direction: column; align-items: center; gap: 5px;
    color: var(--white); font-size: 11px; font-weight: 700;
  }
  .brand-square { width: 14px; height: 14px; background: var(--white); }
  .contact-bar {
    position: absolute; left: 80px; top: 690px; right: 0; height: 28px;
    background: var(--black); display: flex; align-items: center; gap: 12px; padding-left: 6px;
    color: var(--white); font-weight: 700; font-size: 14.5px; white-space: nowrap;
  }
</style>
</head>
<body>

<section class="page front">
  <svg class="page-bg" viewBox="0 0 530 740" preserveAspectRatio="none">
    <defs>
      <linearGradient id="frontRed" x1="0" y1="0" x2="1" y2="1">
        <stop offset="0" stop-color="var(--red)"/>
        <stop offset="1" stop-color="var(--red-dark)"/>
      </linearGradient>
      <linearGradient id="frontGrey" x1="0" y1="0" x2="1" y2="0">
        <stop offset="0" stop-color="#1e1e1e"/>
        <stop offset="0.6" stop-color="#555"/>
        <stop offset="1" stop-color="#9a9a9a"/>
      </linearGradient>
      <linearGradient id="photoTone" x1="0" y1="0" x2="1" y2="1">
        <stop offset="0" stop-color="var(--photo-cream)"/>
        <stop offset="0.5" stop-color="var(--photo-warm)"/>
        <stop offset="1" stop-color="#7a5a40"/>
      </linearGradient>
    </defs>
    <rect width="530" height="740" fill="url(#frontRed)"/>
    <path d="M0 330 Q200 520 530 500 V610 Q300 640 0 400 Z" fill="url(#frontGrey)"/>
    <path d="M0 395 Q250 600 530 610" fill="none" stroke="var(--white)" stroke-width="2"/>
    <path d="M140 740 Q330 650 530 690 V740 Z" fill="url(#frontGrey)"/>
    <path d="M140 740 Q330 650 530 690" fill="none" stroke="var(--white)" stroke-width="2"/>
    <path d="M0 0 H530 V440 Q430 500 300 485 Q120 460 0 390 Z" fill="url(#photoTone)" stroke="var(--white)" stroke-width="3" role="img" aria-label="Photo of a sad pug lying on the floor"/>
  </svg>
  <h1 class="headline"><span class="not">NOT</span><span class="happy">HAPPY?</span></h1>
</section>

<section class="page back">
  <svg class="page-bg" viewBox="0 0 532 744" preserveAspectRatio="none">
    <defs>
      <linearGradient id="backRed" x1="0" y1="0" x2="1" y2="0">
        <stop offset="0" stop-color="var(--red-dark)"/>
        <stop offset="0.5" stop-color="var(--red)"/>
        <stop offset="1" stop-color="var(--red-dark)"/>
      </linearGradient>
    </defs>
    <rect width="532" height="744" fill="var(--charcoal)"/>
    <path d="M0 0 H532 V150 Q300 300 0 330 Z" fill="var(--black)"/>
    <path d="M0 330 Q300 300 532 150 V240 Q320 410 0 420 Z" fill="url(#backRed)"/>
    <path d="M0 335 Q300 305 532 158" fill="none" stroke="var(--white)" stroke-width="2"/>
    <path d="M0 420 Q320 410 532 240 V260 Q320 430 0 440 Z" fill="var(--black)"/>
    <path d="M0 438 Q320 428 532 258" fill="none" stroke="var(--grey-light)" stroke-width="1.5"/>
    <path d="M0 665 Q260 650 532 600 V744 H0 Z" fill="url(#backRed)"/>
    <path d="M0 665 Q260 650 532 600" fill="none" stroke="var(--white)" stroke-width="3"/>
    <rect x="0" y="728" width="532" height="16" fill="var(--red)"/>
  </svg>

  <div class="questions">
    <p class="question">With your current service and advice?</p>
    <div class="answer-box"></div>
    <p class="question">Need a result NOW?</p>
    <div class="answer-box"></div>
    <p class="question">Want a second opinion?</p>
    <div class="answer-box tall"></div>
  </div>

  <div class="intro">
    <p>It is no secret that the greater the exposure a property has to the market, the greater the number of buyers who are aware of the listing. Every property is unique and Tessa ensures that each property has its own tailored marketing plan, so your property stands out from the crowd.</p>
    <p>Whether you’re considering buying locally or internationally, Tessa will work with you to towards understanding those special qualities and those requirements you seek.<br>If you want to combine these components into an advantageous world class real estate transaction, call <span class="agent-name">Tessa Brindley.</span></p>
  </div>

  <div class="agent-photo" role="img" aria-label="Portrait photo of agent Tessa Brindley"></div>
  <div class="name-pill">TESSA BRINDLEY</div>

  <div class="brand"><span class="brand-square"></span><span>Hovex</span></div>
  <div class="contact-bar">
    <span>W: (WEBSITE HERE)</span>
    <span>M: (MOBILE HERE)</span>
    <span>E: (EMAIL HERE)</span>
  </div>
</section>

</body>
</html>
```